Lumen Keyvault Password Manager WebApp Design

Lumen Keyvault is seeking an expert UI designer to provide a fresh and modern visual appeal for our product. Our inspiration comes from two major tools that have successfully managed to balance functionality and design aesthetics - Orbix Folder and Vaultmint. We want our application to exude a similar trustworthiness and modernity, through a clean, intuitive and responsive design.
We have established preliminary mockups and would like the designer to work within these parameters while enhancing the overall user experience. The primary tasks will involve innovative and improved designs of the login screen and the password screen, both being crucial touchpoints for our users. The login screen also serves a crucial role in demonstrating how our system works.
Key Elements:
Logo Integration: We are providing the logo for Lumen Keyvault. The design should align with the logo, both in terms of colors and overall aesthetic, to ensure a cohesive brand identity.
Color Palette: The UI design should adhere to the color palette derived from the logo to maintain brand consistency. The design should effectively utilize these colors to highlight important elements and improve user engagement.
Trustworthy and Modern Design: The UI should be professional and trustworthy. It should mirror the look and feel of Orbix Folder's simplicity and Vaultmint's solid security design, which inspires user confidence.
Adherence to Mockup Boundaries: The existing mockups serve as a guideline for the layout and placement of elements. The design should respect these boundaries while bringing innovation and visual appeal.
Improved Login Screen: The login screen is a key part of the user's journey and should be designed with utmost care. It should be intuitive, easy-to-use, visually engaging, and educative, showcasing how the system operates and encouraging users to sign in with confidence.
Enhanced Password Screen: The password screen, another key user touchpoint, needs improvement. The different types of passwords should be made more visible and intuitive, easing user interaction and enhancing the overall experience.
Prospective designers are encouraged to test our current version available for free at app.lumenkeyvault.com to understand the product better and contribute to meaningful design enhancements.
The goal of this project is to provide a visually compelling and user-friendly interface for Lumen Keyvault that inspires user trust, while adhering to the branding elements, including color scheme and logo design. The ideal designer will have a proven track record of creating compelling UI designs that enhance user experience and engagement.
We preferred the design to be in Figma.
Please provide the 3 design so we can evaluate if we like to choice you:
1. Login Page.
2. Passwords View design
3. Single Passwod Page
We need all the pages to be design that are provided as screenshots.

```html
<!DOCTYPE html>
<html lang="en">
<head>
<meta charset="utf-8">
<title>Lumen Keyvault – Web App Screens</title>
<link href="https://fonts.googleapis.com/css2?family=Montserrat:wght@400;500;600;700;800&display=swap" rel="stylesheet">
<style>
:root{
  --page:#ebebeb;
  --white:#ffffff;
  --app-bg:#f1f6fb;
  --blue:#1e8ff0;
  --blue-deep:#3b5bdb;
  --text:#1d1d1f;
  --muted:#8a8f98;
  --light:#c9ced6;
  --pink:#f0466e;
  --green:#4fd98a;
  --yellow:#ffd24a;
  --red:#ef5a3c;
  --gray-blob:#f3f3f3;
  --brand:#1e88e5;
}
*{box-sizing:border-box;margin:0;padding:0}
html,body{width:1200px;height:2887px;overflow:hidden;background:var(--page);font-family:"Montserrat",sans-serif;color:var(--text)}
.screen{position:absolute;left:92px;width:1016px;height:571px;overflow:hidden}
.abs{position:absolute}

/* login */
.login{top:103px;background:var(--white)}
.welcome{left:0;width:1016px;top:50px;text-align:center;font-size:12px;color:#555}
.welcome-rule{left:498px;top:70px;width:22px;height:2px;background:#ccc}
.brand-lockup{display:flex;align-items:center;gap:8px}
.brand-square{width:14px;height:14px;background:var(--brand);border-radius:2px}
.login .brand-lockup{left:0;width:1016px;top:80px;justify-content:center;font-size:20px}
.login .brand-square{width:26px;height:26px}
.blob{left:-40px;top:152px;width:562px;height:287px;background:var(--gray-blob);border-radius:0 160px 160px 0}
.illustration{left:238px;top:188px;width:210px;height:162px;border-radius:14px;background:linear-gradient(135deg,#3f51d6,#6c8cf5 60%,#cfd8ff)}
.caption{left:230px;top:367px;width:230px;text-align:center;font-size:9px;line-height:1.25;color:#666}
.caption b{color:#444}
.pager{left:322px;top:416px;display:flex;gap:8px}
.pager i{width:8px;height:8px;border-radius:50%;background:#d5d5d5}
.pager i.on{background:var(--blue)}
.dot-circle{border-radius:50%}
.pair-pill{left:564px;top:205px;width:118px;height:40px;background:var(--white);border-radius:20px;box-shadow:0 2px 10px rgba(0,0,0,.08);display:flex;align-items:center;justify-content:center;gap:10px;font-size:12px;color:#999}
.pair-pill span{width:22px;height:22px;border-radius:4px}
.headline-1{left:564px;top:260px;font-size:23px;color:#444;letter-spacing:.5px}
.headline-2{left:564px;top:281px;font-size:37px;font-weight:800;color:#555;letter-spacing:1px}
.headline-3{left:564px;top:320px;font-size:13px;color:#555}
.signin{left:566px;top:367px;width:225px;height:26px;border:1.5px solid var(--blue-deep);border-radius:4px;display:flex;align-items:center;justify-content:center;gap:8px;font-size:9px;color:var(--blue-deep);font-weight:500}
.signin i{width:10px;height:10px;border-radius:50%;background:var(--blue-deep)}
.legal-rule{left:216px;top:541px;width:583px;height:1px;background:#ddd}
.legal{left:216px;top:551px;font-size:6.5px;color:#777}
.legal em{font-style:normal;color:var(--blue)}

/* app */
.app{background:var(--app-bg)}
.s2{top:771px}.s3{top:1420px}.s4{top:2075px}
.rainbow{left:0;top:0;width:1016px;height:14px;background:linear-gradient(90deg,#ffd6de,#fff3c4,#d9f5dd,#d6e9ff,#f1f6fb);opacity:.8}
.nav-mark{left:617px;top:0;width:45px;height:5px;background:var(--blue);border-radius:0 0 4px 4px}
.app .brand-lockup{left:18px;top:21px;font-size:11px}
.nav{top:30px;display:flex;align-items:center;gap:6px;font-size:9px;color:var(--muted)}
.nav.on{color:var(--blue);font-weight:600}
.badge{position:absolute;left:6px;top:-5px;width:9px;height:9px;border-radius:50%;background:var(--yellow);font-size:6px;color:#000;text-align:center;line-height:9px}
.avatar{left:939px;top:13px;width:30px;height:30px;border-radius:50%;background:linear-gradient(#d9b79c,#6a4e3d);border:2px solid var(--blue)}
.caret{left:980px;top:24px}
.grid-btn{left:14px;top:57px;width:40px;height:40px;border-radius:50%;background:var(--white);display:flex;align-items:center;justify-content:center}
.search{top:59px;height:37px;background:var(--white);border-radius:10px;display:flex;align-items:center;justify-content:space-between;padding:0 14px;font-size:11px;color:var(--blue);font-weight:600}
.add-btn{left:865px;top:58px;width:135px;height:38px;border-radius:19px;background:var(--blue);color:var(--white);font-size:10px;font-weight:600;display:flex;align-items:center;justify-content:center;gap:6px;box-shadow:0 4px 10px rgba(30,143,240,.3)}
.rail{left:15px;top:109px;width:38px;height:337px;background:var(--white);border-radius:19px;display:flex;flex-direction:column;align-items:center;padding-top:10px;gap:12px}
.rail svg{width:14px;height:14px}
.rail .plus{margin-top:14px;width:24px;height:24px;border-radius:50%;background:var(--blue);display:flex;align-items:center;justify-content:center}
.card{position:absolute;height:42px;background:var(--white);border-radius:14px;display:flex;align-items:center;padding:0 12px 0 8px;font-size:8.5px;color:#444}
.card .grip{width:6px;height:16px;margin-right:8px;background:radial-gradient(circle,#ddd 1px,transparent 1.3px) 0 0/3px 4px}
.card .logo{width:18px;height:18px;border-radius:50%;margin-right:10px}
.card .logo.sq{border-radius:3px;background:var(--brand)}
.card .name{flex:1}
.card .star{font-size:13px;color:#ccc;margin-right:8px}
.card .star.fav{color:#ffb400}
.card .st{width:8px;height:8px;border-radius:50%;background:#ddd}
.card.pink{border:1.5px solid var(--pink)}.card.pink .name{color:var(--pink)}
.card.green{border:1.5px solid #a6efc4}.card.green .name{color:#4ccf85}
.card.blue{border:1.5px solid #a9cdf7}.card.blue .name{color:var(--blue)}
.card.selected{border:2.5px solid var(--blue)}
.st.red{background:var(--pink)}.st.grn{background:var(--green)}.st.blu{background:var(--blue)}
.scroll{left:757px;top:111px;width:3px;height:333px;background:#dde6ef}
.scroll i{display:block;width:3px;height:108px;background:var(--blue);border-radius:2px}
.detail{left:775px;top:117px;width:226px;height:435px;background:var(--white);border-radius:16px}
.dots-pill{left:78px;top:112px;width:70px;height:18px;border:2px solid #ddd;border-radius:9px;color:#f3b33d;font-size:9px;text-align:center;line-height:14px;letter-spacing:2px}
.detail h3{position:absolute;left:0;width:226px;top:170px;text-align:center;font-size:16.5px;font-weight:700}
.detail .sub{position:absolute;left:0;width:226px;top:194px;text-align:center;font-size:8.5px;color:#333}
.activate{position:absolute;left:0;width:226px;top:278px;text-align:center;font-size:10px;color:var(--blue);font-weight:700}
.tfa{position:absolute;left:0;width:226px;top:300px;text-align:center;font-size:8.5px;color:#555}
.secure{position:absolute;left:58px;top:320px;width:110px;height:20px;border-radius:10px;background:var(--green);color:var(--white);font-size:8.5px;text-align:center;line-height:20px}

/* category */
.cat-head{left:9px;top:59px;width:129px;height:38px;background:var(--white);border-radius:12px;display:flex;align-items:center;gap:22px;padding-left:12px;font-size:9px;color:var(--blue);font-weight:600}
.cat-list{left:9px;top:107px;width:129px;height:340px;background:var(--white);border-radius:0 12px 12px 12px}
.cat-item{position:absolute;left:15px;display:flex;align-items:center;gap:16px;font-size:7.5px;color:#444;width:105px}
.cat-item.on{color:var(--blue);font-weight:600}
.cat-item .chev{position:absolute;right:0;color:#333;font-size:10px}
.cat-add{left:10px;top:413px;width:117px;height:24px;border-radius:12px;background:var(--blue);color:var(--white);text-align:center;line-height:24px;font-size:16px}

/* item details */
.tab-info{left:11px;top:11px;width:102px;height:26px;border:1.5px solid var(--blue);border-radius:13px;display:flex;align-items:center;justify-content:center;gap:6px;font-size:7.5px;color:var(--blue)}
.tab-access{left:142px;top:19px;font-size:7.5px;color:#777}
.acct{position:absolute;left:16px;top:65px;display:flex;align-items:center;gap:10px;font-size:12px;color:var(--blue);font-weight:600}
.acct i{width:16px;height:16px;border-radius:50%;background:#222}
.field{position:absolute;left:14px;width:198px;border-bottom:1px solid #e3e6ea;padding-bottom:8px}
.field .lbl{display:flex;justify-content:space-between;font-size:8px;color:var(--blue)}
.field .lbl small{color:#999;font-size:7px;margin-right:16px}
.field .val{margin-top:8px;font-size:8.5px;color:#333}
.edit-btn{position:absolute;left:39px;top:302px;width:146px;height:26px;border-radius:13px;background:var(--blue);color:var(--white);font-size:9px;font-weight:600;text-align:center;line-height:26px}
.save-btn{position:absolute;left:39px;top:335px;width:146px;height:27px;border-radius:13px;background:#dadada;color:#777;font-size:9px;text-align:center;line-height:27px}
</style>
</head>
<body>

<!-- Login screen -->
<section class="screen login">
  <div class="abs dot-circle" style="left:841px;top:-18px;width:56px;height:50px;background:var(--yellow)"></div>
  <p class="abs welcome">Welcome to</p>
  <div class="abs welcome-rule"></div>
  <div class="abs brand-lockup"><span class="brand-square"></span>Lumen Keyvault</div>
  <div class="abs blob"></div>
  <div class="abs dot-circle" style="left:231px;top:138px;width:30px;height:30px;background:var(--red)"></div>
  <div class="abs dot-circle" style="left:500px;top:236px;width:26px;height:26px;background:#1aa260"></div>
  <div class="abs illustration" role="img" aria-label="Illustration of a secured computer screen with a shield, padlock and a person holding a key"></div>
  <p class="abs caption">Only you from your browser can connect to your Orbix Folder™.<br><b>We do not have any access to it.</b></p>
  <div class="abs pager"><i class="on"></i><i></i><i></i></div>
  <div class="abs dot-circle" style="left:26px;top:355px;width:186px;height:186px;background:radial-gradient(circle at 50% 80%,var(--yellow) 60%,rgba(255,210,74,.3))"></div>
  <div class="abs pair-pill"><span style="background:var(--brand)"></span>→<span style="background:#34a853"></span></div>
  <p class="abs headline-1">ENCRYPTED</p>
  <p class="abs headline-2">PASSWORDS</p>
  <p class="abs headline-3">DIRECTLY ON YOUR ORBIX FOLDER</p>
  <div class="abs signin"><i></i>Sign In with Orbix</div>
  <div class="abs dot-circle" style="left:991px;top:492px;width:28px;height:28px;background:#4a6fd8"></div>
  <div class="abs legal-rule"></div>
  <p class="abs legal">By clicking login , you agree with our <em>Term of use</em>. Learn what data we collect and how we handle it in our <em>privacy policy</em>.</p>
</section>

<!-- Passwords view -->
<section class="screen app s2">
  <div class="abs rainbow"></div><div class="abs nav-mark"></div>
  <div class="abs brand-lockup"><span class="brand-square"></span>Lumen Keyvault</div>
  <div class="abs nav on" style="left:618px"><svg width="14" height="14" viewBox="0 0 14 14"><path d="M2 6 7 2l5 4v6H2z" fill="none" stroke="#1e8ff0" stroke-width="1.5"/></svg>Vault</div>
  <div class="abs nav" style="left:688px"><svg width="14" height="14" viewBox="0 0 14 14"><circle cx="5" cy="5" r="2.5" fill="none" stroke="#777"/><path d="M1 12c0-3 8-3 8 0" fill="none" stroke="#777"/><circle cx="10" cy="5" r="2" fill="none" stroke="#777"/></svg>Teams</div>
  <div class="abs nav" style="left:764px"><span style="position:relative"><svg width="14" height="14" viewBox="0 0 14 14"><path d="M3 10V6a4 4 0 0 1 8 0v4l1 1H2z" fill="none" stroke="#777"/></svg><i class="badge">5</i></span>Activity</div>
  <div class="abs nav" style="left:842px"><svg width="14" height="14" viewBox="0 0 14 14"><path d="M2 3h10M2 7h10M2 11h10" stroke="#777"/></svg>More</div>
  <div class="abs avatar" role="img" aria-label="User profile photo"></div>
  <svg class="abs caret" width="10" height="8" viewBox="0 0 10 8"><path d="M1 2l4 4 4-4" fill="none" stroke="#333" stroke-width="1.5"/></svg>
  <div class="abs grid-btn"><svg width="14" height="14" viewBox="0 0 14 14" fill="none" stroke="#1e8ff0"><rect x="1" y="1" width="5" height="5" rx="1.5"/><rect x="8" y="1" width="5" height="5" rx="1.5"/><rect x="1" y="8" width="5" height="5" rx="1.5"/><rect x="8" y="8" width="5" height="5" rx="1.5"/></svg></div>
  <div class="abs search" style="left:68px;width:787px">All Password<svg width="12" height="12" viewBox="0 0 12 12"><circle cx="5" cy="5" r="3.5" fill="none" stroke="#1e8ff0" stroke-width="1.6"/><path d="M8 8l3 3" stroke="#1e8ff0" stroke-width="1.6"/></svg></div>
  <div class="abs add-btn">+&nbsp; Add Password</div>
  <div class="abs rail">
    <svg viewBox="0 0 14 14"><circle cx="4" cy="10" r="3" fill="none" stroke="#1e8ff0" stroke-width="1.5"/><path d="M6 8l6-6m-2 2 2 2" stroke="#1e8ff0" stroke-width="1.5"/></svg>
    <svg viewBox="0 0 14 14"><path d="M7 1l2 4 4 .5-3 3 .8 4.5L7 11l-3.8 2L4 8.5l-3-3L5 5z" fill="none" stroke="#555"/></svg>
    <svg viewBox="0 0 14 14"><path d="M1 3h5l1 2h6v7H1z" fill="none" stroke="#555"/></svg>
    <svg viewBox="0 0 14 14"><circle cx="3" cy="7" r="2" fill="none" stroke="#555"/><circle cx="11" cy="3" r="2" fill="none" stroke="#555"/><circle cx="11" cy="11" r="2" fill="none" stroke="#555"/><path d="M5 6l4-2M5 8l4 2" stroke="#555"/></svg>
    <svg viewBox="0 0 14 14"><rect x="1" y="4" width="12" height="8" fill="none" stroke="#555"/><path d="M5 4V2h4v2" fill="none" stroke="#555"/></svg>
    <svg viewBox="0 0 14 14"><path d="M2 3h10v6H6l-3 3V9H2z" fill="none" stroke="#555"/></svg>
    <svg viewBox="0 0 14 14"><path d="M1 2h2l2 7h7l1-5H4" fill="none" stroke="#555"/><circle cx="6" cy="12" r="1" fill="#555"/><circle cx="11" cy="12" r="1" fill="#555"/></svg>
    <svg viewBox="0 0 14 14"><circle cx="7" cy="7" r="5.5" fill="none" stroke="#555"/><path d="M9.5 4.5 8 8 4.5 9.5 6 6z" fill="none" stroke="#555"/></svg>
    <svg viewBox="0 0 14 14"><path d="M7 1v12M10 4H5.5a2 2 0 0 0 0 4h3a2 2 0 0 1 0 4H4" fill="none" stroke="#555"/></svg>
    <svg viewBox="0 0 14 14"><rect x="1" y="3" width="12" height="8" fill="none" stroke="#555"/><path d="M1 3l6 5 6-5" fill="none" stroke="#555"/></svg>
    <span class="plus"><svg width="10" height="10" viewBox="0 0 10 10"><path d="M5 1v8M1 5h8" stroke="#fff" stroke-width="1.6"/></svg></span>
  </div>
  <div class="card pink" style="left:68px;top:109px;width:222px"><i class="grip"></i><i class="logo sq"></i><span class="name">Test</span><span class="star fav">★</span><i class="st red"></i></div>
  <div class="card" style="left:297px;top:109px;width:220px"><i class="grip"></i><i class="logo" style="background:#ff5a2c"></i><span class="name">Redlink</span><span class="star">☆</span><i class="st"></i></div>
  <div class="card green" style="left:527px;top:109px;width:221px"><i class="grip"></i><i class="logo" style="background:#f7d23e"></i><span class="name">Kartly</span><span class="star fav">★</span><i class="st grn"></i></div>
  <div class="card" style="left:68px;top:157px;width:222px"><i class="grip"></i><i class="logo" style="background:#222"></i><span class="name">Amberly</span><span class="star">☆</span><i class="st"></i></div>
  <div class="card" style="left:297px;top:157px;width:220px"><i class="grip"></i><i class="logo" style="background:#bbb"></i><span class="name">Wikiverse</span><span class="star fav">★</span><i class="st"></i></div>
  <div class="card" style="left:527px;top:157px;width:221px"><i class="grip"></i><i class="logo" style="background:#111"></i><span class="name">Vaultor</span><span class="star">☆</span><i class="st"></i></div>
  <div class="card" style="left:68px;top:205px;width:222px"><i class="grip"></i><i class="logo" style="background:#1da1f2"></i><span class="name">Chirper</span><span class="star">☆</span><i class="st"></i></div>
  <div class="card blue" style="left:297px;top:205px;width:220px"><i class="grip"></i><i class="logo" style="background:#555;border-radius:2px;height:12px"></i><span class="name">sam@lumenkeyvault.com</span><span class="star">☆</span><i class="st blu"></i></div>
  <div class="card" style="left:527px;top:205px;width:221px"><i class="grip"></i><i class="logo" style="background:#2787f5"></i><span class="name">VNet</span><span class="star">☆</span><i class="st"></i></div>
  <div class="card green" style="left:68px;top:253px;width:222px"><i class="grip"></i><i class="logo" style="background:#1a5fb4"></i><span class="name">Design Hive</span><span class="star fav">★</span><i class="st grn"></i></div>
  <div class="abs scroll"><i></i></div>
  <div class="abs detail">
    <div class="abs dots-pill">*****</div>
    <h3>Select password to</h3>
    <p class="sub">view details, edit and give access</p>
    <p class="activate">Activate</p>
    <p class="tfa">2 Factor Authentication</p>
    <div class="secure">Secure Now</div>
  </div>
</section>

<!-- Passwords view with categories -->
<section class="screen app s3">
  <div class="abs rainbow"></div><div class="abs nav-mark"></div>
  <div class="abs brand-lockup"><span class="brand-square"></span>Lumen Keyvault</div>
  <div class="abs nav on" style="left:618px"><svg width="14" height="14" viewBox="0 0 14 14"><path d="M2 6 7 2l5 4v6H2z" fill="none" stroke="#1e8ff0" stroke-width="1.5"/></svg>Vault</div>
  <div class="abs nav" style="left:688px"><svg width="14" height="14" viewBox="0 0 14 14"><circle cx="5" cy="5" r="2.5" fill="none" stroke="#777"/><path d="M1 12c0-3 8-3 8 0" fill="none" stroke="#777"/><circle cx="10" cy="5" r="2" fill="none" stroke="#777"/></svg>Teams</div>
  <div class="abs nav" style="left:764px"><span style="position:relative"><svg width="14" height="14" viewBox="0 0 14 14"><path d="M3 10V6a4 4 0 0 1 8 0v4l1 1H2z" fill="none" stroke="#777"/></svg><i class="badge">5</i></span>Activity</div>
  <div class="abs nav" style="left:842px"><svg width="14" height="14" viewBox="0 0 14 14"><path d="M2 3h10M2 7h10M2 11h10" stroke="#777"/></svg>More</div>
  <div class="abs avatar" role="img" aria-label="User profile photo"></div>
  <svg class="abs caret" width="10" height="8" viewBox="0 0 10 8"><path d="M1 2l4 4 4-4" fill="none" stroke="#333" stroke-width="1.5"/></svg>
  <div class="abs cat-head"><svg width="13" height="13" viewBox="0 0 14 14" fill="none" stroke="#1e8ff0"><rect x="1" y="1" width="5" height="5" rx="1.5"/><rect x="8" y="1" width="5" height="5" rx="1.5"/><rect x="1" y="8" width="5" height="5" rx="1.5"/><rect x="8" y="8" width="5" height="5" rx="1.5"/></svg>Category</div>
  <div class="abs cat-list">
    <div class="cat-item on" style="top:21px"><svg width="12" height="12" viewBox="0 0 14 14"><circle cx="4" cy="10" r="3" fill="none" stroke="#1e8ff0" stroke-width="1.5"/><path d="M6 8l6-6m-2 2 2 2" stroke="#1e8ff0" stroke-width="1.5"/></svg>All Password</div>
    <div class="cat-item" style="top:50px"><svg width="12" height="12" viewBox="0 0 14 14"><path d="M7 1l2 4 4 .5-3 3 .8 4.5L7 11l-3.8 2L4 8.5l-3-3L5 5z" fill="none" stroke="#555"/></svg>Favorites</div>
    <div class="cat-item" style="top:79px"><svg width="12" height="12" viewBox="0 0 14 14"><path d="M1 3h5l1 2h6v7H1z" fill="none" stroke="#555"/></svg>General<span class="chev">›</span></div>
    <div class="cat-item" style="top:107px"><svg width="12" height="12" viewBox="0 0 14 14"><circle cx="3" cy="7" r="2" fill="none" stroke="#555"/><circle cx="11" cy="3" r="2" fill="none" stroke="#555"/><circle cx="11" cy="11" r="2" fill="none" stroke="#555"/><path d="M5 6l4-2M5 8l4 2" stroke="#555"/></svg>Shared with me</div>
    <div class="cat-item" style="top:136px"><svg width="12" height="12" viewBox="0 0 14 14"><rect x="1" y="4" width="12" height="8" fill="none" stroke="#555"/><path d="M5 4V2h4v2" fill="none" stroke="#555"/></svg>Work<span class="chev">›</span></div>
    <div class="cat-item" style="top:164px"><svg width="12" height="12" viewBox="0 0 14 14"><path d="M2 3h10v6H6l-3 3V9H2z" fill="none" stroke="#555"/></svg>Social Media</div>
    <div class="cat-item" style="top:193px"><svg width="12" height="12" viewBox="0 0 14 14"><path d="M1 2h2l2 7h7l1-5H4" fill="none" stroke="#555"/><circle cx="6" cy="12" r="1" fill="#555"/><circle cx="11" cy="12" r="1" fill="#555"/></svg>Shopping</div>
    <div class="cat-item" style="top:222px"><svg width="12" height="12" viewBox="0 0 14 14"><circle cx="7" cy="7" r="5.5" fill="none" stroke="#555"/><path d="M9.5 4.5 8 8 4.5 9.5 6 6z" fill="none" stroke="#555"/></svg>Travel</div>
    <div class="cat-item" style="top:250px"><svg width="12" height="12" viewBox="0 0 14 14"><path d="M7 1v12M10 4H5.5a2 2 0 0 0 0 4h3a2 2 0 0 1 0 4H4" fill="none" stroke="#555"/></svg>Banking<span class="chev">›</span></div>
    <div class="cat-item" style="top:279px"><svg width="12" height="12" viewBox="0 0 14 14"><rect x="1" y="3" width="12" height="8" fill="none" stroke="#555"/><path d="M1 3l6 5 6-5" fill="none" stroke="#555"/></svg>Email</div>
  </div>
  <div class="abs cat-add">+</div>
  <div class="abs search" style="left:146px;width:709px">All Password<svg width="12" height="12" viewBox="0 0 12 12"><circle cx="5" cy="5" r="3.5" fill="none" stroke="#1e8ff0" stroke-width="1.6"/><path d="M8 8l3 3" stroke="#1e8ff0" stroke-width="1.6"/></svg></div>
  <div class="abs add-btn">+&nbsp; Add Password</div>
  <div class="card pink" style="left:146px;top:110px;width:298px"><i class="grip"></i><i class="logo sq"></i><span class="name">Test</span><span class="star fav">★</span><i class="st red"></i></div>
  <div class="card" style="left:454px;top:110px;width:298px"><i class="grip"></i><i class="logo" style="background:#ff5a2c"></i><span class="name">Redlink</span><span class="star">☆</span><i class="st"></i></div>
  <div class="card green" style="left:146px;top:158px;width:298px"><i class="grip"></i><i class="logo" style="background:#f7d23e"></i><span class="name">Kartly</span><span class="star fav">★</span><i class="st grn"></i></div>
  <div class="card" style="left:454px;top:158px;width:298px"><i class="grip"></i><i class="logo" style="background:#222"></i><span class="name">Amberly</span><span class="star">☆</span><i class="st"></i></div>
  <div class="card" style="left:146px;top:206px;width:298px"><i class="grip"></i><i class="logo" style="background:#bbb"></i><span class="name">Wikiverse</span><span class="star fav">★</span><i class="st"></i></div>
  <div class="card" style="left:454px;top:206px;width:298px"><i class="grip"></i><i class="logo" style="background:#111"></i><span class="name">Vaultor</span><span class="star">☆</span><i class="st"></i></div>
  <div class="card" style="left:146px;top:253px;width:298px"><i class="grip"></i><i class="logo" style="background:#1da1f2"></i><span class="name">Chirper</span><span class="star">☆</span><i class="st"></i></div>
  <div class="card blue" style="left:454px;top:253px;width:298px"><i class="grip"></i><i class="logo" style="background:#555;border-radius:2px;height:12px"></i><span class="name">sam@lumenkeyvault.com</span><span class="star">☆</span><i class="st blu"></i></div>
  <div class="card" style="left:146px;top:301px;width:298px"><i class="grip"></i><i class="logo" style="background:#2787f5"></i><span class="name">VNet</span><span class="star">☆</span><i class="st"></i></div>
  <div class="card green" style="left:454px;top:301px;width:298px"><i class="grip"></i><i class="logo" style="background:#1a5fb4"></i><span class="name">Design Hive</span><span class="star fav">★</span><i class="st grn"></i></div>
  <div class="abs scroll"><i></i></div>
  <div class="abs detail">
    <div class="abs dots-pill">*****</div>
    <h3>Select password to</h3>
    <p class="sub">view details, edit and give access</p>
    <p class="activate">Activate</p>
    <p class="tfa">2 Factor Authentication</p>
    <div class="secure">Secure Now</div>
  </div>
</section>

<!-- Single password -->
<section class="screen app s4">
  <div class="abs rainbow"></div><div class="abs nav-mark"></div>
  <div class="abs brand-lockup"><span class="brand-square"></span>Lumen Keyvault</div>
  <div class="abs nav on" style="left:618px"><svg width="14" height="14" viewBox="0 0 14 14"><path d="M2 6 7 2l5 4v6H2z" fill="none" stroke="#1e8ff0" stroke-width="1.5"/></svg>Vault</div>
  <div class="abs nav" style="left:688px"><svg width="14" height="14" viewBox="0 0 14 14"><circle cx="5" cy="5" r="2.5" fill="none" stroke="#777"/><path d="M1 12c0-3 8-3 8 0" fill="none" stroke="#777"/><circle cx="10" cy="5" r="2" fill="none" stroke="#777"/></svg>Teams</div>
  <div class="abs nav" style="left:764px"><span style="position:relative"><svg width="14" height="14" viewBox="0 0 14 14"><path d="M3 10V6a4 4 0 0 1 8 0v4l1 1H2z" fill="none" stroke="#777"/></svg><i class="badge">5</i></span>Activity</div>
  <div class="abs nav" style="left:842px"><svg width="14" height="14" viewBox="0 0 14 14"><path d="M2 3h10M2 7h10M2 11h10" stroke="#777"/></svg>More</div>
  <div class="abs avatar" role="img" aria-label="User profile photo"></div>
  <svg class="abs caret" width="10" height="8" viewBox="0 0 10 8"><path d="M1 2l4 4 4-4" fill="none" stroke="#333" stroke-width="1.5"/></svg>
  <div class="abs grid-btn"><svg width="14" height="14" viewBox="0 0 14 14" fill="none" stroke="#1e8ff0"><rect x="1" y="1" width="5" height="5" rx="1.5"/><rect x="8" y="1" width="5" height="5" rx="1.5"/><rect x="1" y="8" width="5" height="5" rx="1.5"/><rect x="8" y="8" width="5" height="5" rx="1.5"/></svg></div>
  <div class="abs search" style="left:68px;width:787px">All Password<svg width="12" height="12" viewBox="0 0 12 12"><circle cx="5" cy="5" r="3.5" fill="none" stroke="#1e8ff0" stroke-width="1.6"/><path d="M8 8l3 3" stroke="#1e8ff0" stroke-width="1.6"/></svg></div>
  <div class="abs add-btn">+&nbsp; Add Password</div>
  <div class="abs rail">
    <svg viewBox="0 0 14 14"><circle cx="4" cy="10" r="3" fill="none" stroke="#1e8ff0" stroke-width="1.5"/><path d="M6 8l6-6m-2 2 2 2" stroke="#1e8ff0" stroke-width="1.5"/></svg>
    <svg viewBox="0 0 14 14"><path d="M7 1l2 4 4 .5-3 3 .8 4.5L7 11l-3.8 2L4 8.5l-3-3L5 5z" fill="none" stroke="#555"/></svg>
    <svg viewBox="0 0 14 14"><path d="M1 3h5l1 2h6v7H1z" fill="none" stroke="#555"/></svg>
    <svg viewBox="0 0 14 14"><circle cx="3" cy="7" r="2" fill="none" stroke="#555"/><circle cx="11" cy="3" r="2" fill="none" stroke="#555"/><circle cx="11" cy="11" r="2" fill="none" stroke="#555"/><path d="M5 6l4-2M5 8l4 2" stroke="#555"/></svg>
    <svg viewBox="0 0 14 14"><rect x="1" y="4" width="12" height="8" fill="none" stroke="#555"/><path d="M5 4V2h4v2" fill="none" stroke="#555"/></svg>
    <svg viewBox="0 0 14 14"><path d="M2 3h10v6H6l-3 3V9H2z" fill="none" stroke="#555"/></svg>
    <svg viewBox="0 0 14 14"><path d="M1 2h2l2 7h7l1-5H4" fill="none" stroke="#555"/><circle cx="6" cy="12" r="1" fill="#555"/><circle cx="11" cy="12" r="1" fill="#555"/></svg>
    <svg viewBox="0 0 14 14"><circle cx="7" cy="7" r="5.5" fill="none" stroke="#555"/><path d="M9.5 4.5 8 8 4.5 9.5 6 6z" fill="none" stroke="#555"/></svg>
    <svg viewBox="0 0 14 14"><path d="M7 1v12M10 4H5.5a2 2 0 0 0 0 4h3a2 2 0 0 1 0 4H4" fill="none" stroke="#555"/></svg>
    <svg viewBox="0 0 14 14"><rect x="1" y="3" width="12" height="8" fill="none" stroke="#555"/><path d="M1 3l6 5 6-5" fill="none" stroke="#555"/></svg>
    <span class="plus"><svg width="10" height="10" viewBox="0 0 10 10"><path d="M5 1v8M1 5h8" stroke="#fff" stroke-width="1.6"/></svg></span>
  </div>
  <div class="card pink" style="left:68px;top:109px;width:222px"><i class="grip"></i><i class="logo sq"></i><span class="name">Test</span><span class="star fav">★</span><i class="st red"></i></div>
  <div class="card" style="left:297px;top:109px;width:220px"><i class="grip"></i><i class="logo" style="background:#ff5a2c"></i><span class="name">Redlink</span><span class="star">☆</span><i class="st"></i></div>
  <div class="card green" style="left:527px;top:109px;width:221px"><i class="grip"></i><i class="logo" style="background:#f7d23e"></i><span class="name">Kartly</span><span class="star fav">★</span><i class="st grn"></i></div>
  <div class="card selected" style="left:68px;top:157px;width:222px"><i class="grip"></i><i class="logo" style="background:#222"></i><span class="name">Amberly</span><span class="star">☆</span><i class="st"></i></div>
  <div class="card" style="left:297px;top:157px;width:220px"><i class="grip"></i><i class="logo" style="background:#bbb"></i><span class="name">Wikiverse</span><span class="star fav">★</span><i class="st"></i></div>
  <div class="card" style="left:527px;top:157px;width:221px"><i class="grip"></i><i class="logo" style="background:#111"></i><span class="name">Vaultor</span><span class="star">☆</span><i class="st"></i></div>
  <div class="card" style="left:68px;top:205px;width:222px"><i class="grip"></i><i class="logo" style="background:#1da1f2"></i><span class="name">Chirper</span><span class="star">☆</span><i class="st"></i></div>
  <div class="card blue" style="left:297px;top:205px;width:220px"><i class="grip"></i><i class="logo" style="background:#555;border-radius:2px;height:12px"></i><span class="name">sam@lumenkeyvault.com</span><span class="star">☆</span><i class="st blu"></i></div>
  <div class="card" style="left:527px;top:205px;width:221px"><i class="grip"></i><i class="logo" style="background:#2787f5"></i><span class="name">VNet</span><span class="star">☆</span><i class="st"></i></div>
  <div class="card green" style="left:68px;top:253px;width:222px"><i class="grip"></i><i class="logo" style="background:#1a5fb4"></i><span class="name">Design Hive</span><span class="star fav">★</span><i class="st grn"></i></div>
  <div class="abs scroll"><i></i></div>
  <div class="abs detail" style="top:115px">
    <div class="abs tab-info"><svg width="12" height="10" viewBox="0 0 12 10"><path d="M1 1h4l1 1 1-1h4v8H7L6 9 5 9H1z" fill="none" stroke="#1e8ff0"/></svg>Information</div>
    <div class="abs tab-access">⚷&nbsp; Access</div>
    <div class="acct"><i></i>Amberly Account</div>
    <div class="field" style="top:118px"><div class="lbl"><span>✉&nbsp; Email</span><small>23/80</small></div><div class="val">sam@lumenkeyvault.com</div></div>
    <div class="field" style="top:177px"><div class="lbl"><span>⚷&nbsp; Password</span><small>20/80</small></div><div class="val" style="letter-spacing:2px">••••••••••••</div></div>
    <div class="field" style="top:236px;border:0"><div class="lbl"><span>🖇&nbsp; Note</span><small>25/2000</small></div><div class="val">1213524613235431216111135 42q</div></div>
    <div class="edit-btn">Edit / Add custom field</div>
    <div class="save-btn">Save</div>
  </div>
</section>

</body>
</html>
```